Start up Dialysis Clinic needs its first website - Torvane Health

Create a visually appealing and user-friendly website for Torvane Health, a dialysis clinic located in Port Calder, Halvern Isle. The website should effectively communicate our services to local, regional, and international patients, providing essential information and fostering trust and engagement..
Key Goals:

1. Informative: Provide comprehensive information about our services, facility, and team.
2. User-Friendly: Ensure the website is easy to navigate, with a clear structure and accessible content.
3. Engaging: Create a visually appealing design that reflects the professionalism and care of Torvane Health.
4. Responsive: Ensure the website is fully responsive and performs well on all devices, including desktops, tablets, and smartphones.
5. Trust-Building: Include testimonials, credentials, and patient resources to build trust with potential patients.
Scope of Work:

1. Home Page: An inviting and informative landing page that provides an overview of our clinic, mission, and services. Include a call to action for more information and contact details.
2. About Us: A detailed page about Torvane Health, including our mission, vision, team, and facility tour.
3. Services: A comprehensive page describing the dialysis services we offer, including Hemodialysis, Peritoneal Dialysis, and Home Hemodialysis.
4. Patient Information: A resourceful section with guides for new patients, FAQs, insurance and billing information, and downloadable forms.
5. Resources: Educational content about kidney health, dialysis options, diet and nutrition tips, and support groups.
6. Contact Us: A contact page with our address, phone number, email, office hours, a contact form, and a map.

```html
<!DOCTYPE html>
<html lang="en">
<head>
<meta charset="utf-8">
<title>Torvane Health</title>
<link href="https://fonts.googleapis.com/css2?family=Exo+2:wght@500;600;700&family=Arimo:ital,wght@0,400;0,700;1,400&family=Roboto:wght@400;500;700&display=swap" rel="stylesheet">
<style>
:root{
  --blue:#3f74b8;
  --green:#6ba648;
  --text:#2f2f2f;
  --pale:#eef3f9;
  --white:#fff;
  --footer:#3f7cc4;
  --grad:linear-gradient(90deg,var(--blue) 0%,#4f8c8a 50%,var(--green) 100%);
}
*{margin:0;padding:0;box-sizing:border-box}
html,body{width:1200px;height:4313px;overflow:hidden}
body{position:relative;background:var(--white);font-family:"Arimo",Arial,sans-serif;color:var(--text)}
.abs{position:absolute}
.heading{font-family:"Exo 2",sans-serif;font-weight:600;text-transform:uppercase;line-height:1.05}
.c-blue{color:var(--blue)}.c-green{color:var(--green)}

/* top bar */
.topbar{left:418px;top:0;width:782px;height:43px;background:var(--grad);clip-path:polygon(26px 0,100% 0,100% 100%,0 100%);color:#fff;font-family:"Roboto",sans-serif;font-size:16px}
.topbar span{position:absolute;top:12px;white-space:nowrap}
.topbar .phone-ico{position:absolute;left:34px;top:13px}
.topbar .divider{position:absolute;left:270px;top:6px;width:1px;height:31px;background:rgba(255,255,255,.5)}
.brand{left:120px;top:18px;width:120px;display:flex;flex-direction:column;align-items:center;gap:6px}
.brand .mark{width:28px;height:28px;border:3px solid var(--blue)}
.brand .name{font-family:"Exo 2",sans-serif;font-weight:700;font-size:17px;line-height:18px;color:var(--blue);text-align:center;letter-spacing:.5px}
.nav{top:74px;left:0;font-family:"Roboto",sans-serif;font-size:16px;color:#333}
.nav a{position:absolute;white-space:nowrap;color:inherit;text-decoration:none}
.nav a.active{color:var(--blue)}
.navline{left:0;top:119px;width:1200px;height:1px;background:#e3e3e3}

/* hero */
.hero{left:0;top:120px;width:1200px;height:489px;overflow:hidden;background:linear-gradient(100deg,#6f6a58 0%,#8a8b6a 35%,#5f7d5a 60%,#90a677 80%,#6c8d5c 100%)}
.hero-title{left:125px;top:155px;font-family:"Exo 2",sans-serif;font-weight:500;font-size:50px;color:#fff;white-space:nowrap}
.hero-sub{left:128px;top:222px;font-size:21px;line-height:26px;color:#fff}
.btn-outline{left:127px;top:293px;width:181px;height:54px;border:2px solid #fff;border-radius:27px;color:#fff;font-family:"Roboto",sans-serif;font-weight:700;font-size:16px;display:flex;align-items:center;justify-content:center}

/* about */
.about-frame{left:75px;top:753px;width:420px;height:360px;border:5px solid;border-image:linear-gradient(135deg,var(--green),var(--blue)) 1}
.about-photo{left:105px;top:781px;width:363px;height:304px;background:linear-gradient(135deg,#e6e6e4,#b8b6b0 50%,#d9dad6)}
.h2{font-size:42px;white-space:nowrap}
.body-copy{font-size:17px;line-height:21px;color:#333}
.deco-square{left:1002px;top:904px;width:198px;height:204px;border:6px solid var(--blue);border-right:none}

/* mission */
.mission-photo{left:579px;top:1272px;width:482px;height:564px;background:linear-gradient(160deg,#e9f4f8,#c9e2ea 45%,#eef1f0 100%)}
.mission-line{left:909px;top:1599px;width:171px;height:254px;border-right:6px solid var(--blue);border-bottom:6px solid var(--blue)}
.mission-box{left:105px;top:1381px;width:538px;height:347px;background:linear-gradient(90deg,var(--blue),var(--green));color:#fff;padding:72px 70px 0}
.mission-box h2{font-size:42px;margin-bottom:22px}
.mission-box p{font-size:17px;line-height:21px}

/* services */
.services{left:0;top:2014px;width:1200px;height:728px;background:var(--pale)}
.services-title{left:0;top:2086px;width:1200px;text-align:center;font-size:40px}
.card{top:2183px;width:290px;height:440px;background:#fff;box-shadow:0 4px 14px rgba(0,0,0,.06);text-align:center}
.card .photo{width:290px;height:207px;clip-path:polygon(0 0,100% 0,100% 88%,0 100%)}
.card h3{font-weight:700;font-size:26px;line-height:28px;color:var(--green);margin-top:12px}
.card p{font-size:15px;line-height:19px;color:#555;padding:0 30px;margin-top:12px;height:80px}
.card .pill{position:absolute;left:80px;top:363px;display:flex;align-items:center;justify-content:center;width:131px;height:42px;border-radius:21px;background:var(--blue);color:#fff;font-family:"Roboto",sans-serif;font-weight:700;font-size:13px}

/* testimonials */
.testimonials{left:0;top:2742px;width:1200px;height:450px;overflow:hidden;background:linear-gradient(90deg,#3f74b8 0%,#4c8a8d 55%,#6ba648 100%)}
.test-title{left:0;top:2822px;width:1200px;text-align:center;color:#fff;font-size:42px}
.avatar-ring{left:265px;top:2911px;width:178px;height:178px;border-radius:50%;border:2px solid rgba(255,255,255,.85)}
.avatar{left:277px;top:2923px;width:154px;height:154px;border-radius:50%;background:linear-gradient(160deg,#cfd8e3,#8aa0b8)}
.quote{left:497px;top:2921px;width:540px;font-style:italic;font-size:21px;line-height:28px;color:#fff}
.quote-name{left:497px;top:3053px;font-family:"Roboto",sans-serif;font-weight:700;font-size:19px;color:#fff}

/* why */
.why-photo{left:169px;top:3356px;width:370px;height:384px;background:linear-gradient(135deg,#4f8c8a,#3f74b8 60%,#6ba648)}
.why-inner{left:199px;top:3386px;width:310px;height:324px;background:linear-gradient(160deg,#9fc2c4,#6e9aa8 50%,#8fb29a)}

/* footer */
.footer{left:0;top:3867px;width:1200px;height:446px;background:var(--footer);color:#fff}
.foot-brand{left:122px;top:3948px;width:200px;display:flex;flex-direction:column;align-items:center;gap:14px}
.foot-brand .mark{width:70px;height:70px;border:4px solid #fff}
.foot-brand .name{font-family:"Exo 2",sans-serif;font-weight:700;font-size:28px;line-height:30px;color:#fff;text-align:center;letter-spacing:1px}
.foot-h{top:3946px;font-family:"Exo 2",sans-serif;font-weight:600;font-size:22px;color:#fff;text-transform:uppercase}
.contact-row{display:flex;gap:12px;position:absolute;font-size:14px;line-height:18px;color:#fff;white-space:nowrap}
.contact-row .ico{width:34px;height:34px;border:1px solid rgba(255,255,255,.8);display:flex;align-items:center;justify-content:center;flex:none}
.links{left:941px;top:3998px;font-size:14px;line-height:25.5px;color:#fff;list-style:none}
.foot-rule{left:380px;top:4229px;width:692px;height:1px;background:rgba(255,255,255,.45)}
.copyright{left:0;top:4263px;width:1200px;text-align:center;font-size:15px;color:#fff}
</style>
</head>
<body>

<!-- header -->
<div class="abs topbar">
  <svg class="phone-ico" width="18" height="18" viewBox="0 0 24 24" fill="none" stroke="#fff" stroke-width="2"><path d="M5 3h4l2 5-3 2a12 12 0 0 0 6 6l2-3 5 2v4a2 2 0 0 1-2 2A17 17 0 0 1 3 5a2 2 0 0 1 2-2z"/></svg>
  <span style="left:60px">Call Us: 555 010 2040</span>
  <i class="divider"></i>
  <span style="left:300px">Testimonials</span>
  <span style="left:420px">Credentials</span>
  <span style="left:534px">Patient Resources</span>
</div>
<div class="abs brand"><i class="mark"></i><span class="name">TORVANE<br>HEALTH</span></div>
<nav class="abs nav">
  <a class="active" style="left:303px">HOME</a>
  <a style="left:395px">ABOUT US</a>
  <a style="left:520px">SERVICES</a>
  <a style="left:639px">PATIENT INFORMATION</a>
  <a style="left:859px">RESOURCES</a>
  <a style="left:996px">CONTACT US</a>
</nav>
<div class="abs navline"></div>

<!-- hero -->
<section class="abs hero" role="img" aria-label="Photo of a smiling woman with curly hair in a bright green interior">
  <svg class="abs" style="left:0;top:0" width="1200" height="489" viewBox="0 0 1200 489">
    <polygon points="0,0 560,0 420,489 0,489" fill="#3f74b8" opacity=".35"/>
    <polygon points="460,0 560,0 420,489 330,489" fill="#8fbf6a" opacity=".35"/>
  </svg>
  <div class="abs hero-title">Torvane Health</div>
  <div class="abs hero-sub">Lorem ipsum dolor sit amet consec<br>tetur adipiscing elit sed do.</div>
  <div class="abs btn-outline">READ MORE</div>
</section>

<!-- about -->
<div class="abs about-frame"></div>
<div class="abs about-photo" role="img" aria-label="Photo of a patient in a treatment chair with a nurse beside her"></div>
<h2 class="abs heading h2" style="left:541px;top:750px"><span class="c-blue">About</span><br><span class="c-green">Torvane Health</span></h2>
<div class="abs body-copy" style="left:574px;top:866px;width:410px">
  <p>Lorem ipsum dolor sit amet, consectetur adipiscing elit, sed do eiusmod tempor incididunt ut laboreet dolore magna aliqua. Quis ipsum suspendisse ultrices gravida. Risus commodo viverra maece nas accumsan lacus vel facilisis.</p>
  <p style="margin-top:21px">Lorem ipsum dolor sit amet, consectetur adipiscin gelit, sed do eiusmod tempor incididunt ut laboret dolore magna aliqua. Quis ipsum suspendisse ultrices gravida. Risus commodo viverra maece nas accumsan lacus vel facilisis.</p>
</div>
<div class="abs deco-square"></div>

<!-- mission -->
<div class="abs mission-line"></div>
<div class="abs mission-photo" role="img" aria-label="Photo of a bright dialysis room with machines and reclining chairs"></div>
<div class="abs mission-box">
  <h2 class="heading">Mission</h2>
  <p>Lorem ipsum dolor sit amet, consectetur adipiscing elit, sed do eiusmod tempor incididunt ut laboreet dolore magna aliqua. Quis ipsum suspendisslore ultrices gravida. Risus commodo viverra maecloe nas accumsan lacus vel facilisirem ipsum dolor sit amet, consectetur adipiscingeli.</p>
</div>

<!-- services -->
<section class="abs services"></section>
<h2 class="abs heading services-title"><span class="c-blue">Services</span> <span class="c-green">We Offer</span></h2>
<article class="abs card" style="left:127px">
  <div class="photo" role="img" aria-label="Photo of a doctor with a patient beside a monitor" style="background:linear-gradient(135deg,#dfe6ee,#9fb5c9)"></div>
  <h3>Hemodialysis</h3>
  <p>Lorem ipsum dolor sit ametco nsectetur adipiscing elit, sed do eiusmod tempor incididunt ut laboreet dolore magna.</p>
  <span class="pill">READ MORE</span>
</article>
<article class="abs card" style="left:455px">
  <div class="photo" role="img" aria-label="Photo of a patient's arm connected to dialysis tubing" style="background:linear-gradient(135deg,#c94a4a,#8fa8c8 60%,#c7d3e0)"></div>
  <h3>Peritoneal<br>Dialysis</h3>
  <p>Lorem ipsum dolor sit ametco nsectetur adipiscing elit, sed do eiusmod tempor incididu.</p>
  <span class="pill">READ MORE</span>
</article>
<article class="abs card" style="left:782px">
  <div class="photo" role="img" aria-label="Photo of a patient at a home dialysis machine with a clinician" style="background:linear-gradient(135deg,#b7a58a,#d8d4cb 55%,#a9b6c2)"></div>
  <h3>Home<br>Hemodialysis</h3>
  <p>Lorem ipsum dolor sit ametco nsectetur adipiscing elit, sed do eiusmod tempor incididu.</p>
  <span class="pill">READ MORE</span>
</article>

<!-- testimonials -->
<section class="abs testimonials">
  <svg class="abs" style="left:0;top:0" width="1200" height="450" viewBox="0 0 1200 450">
    <path d="M0 150 C80 180 110 260 180 310 C230 350 230 420 240 450 L0 450Z" fill="#fff" opacity=".1"/>
    <path d="M980 0 C940 60 920 130 1000 130 C1080 130 1140 190 1200 260 L1200 0Z" fill="#fff" opacity=".1"/>
  </svg>
</section>
<h2 class="abs heading test-title">Testimonials</h2>
<div class="abs avatar-ring"></div>
<div class="abs avatar" role="img" aria-label="Portrait photo of the reviewer"></div>
<p class="abs quote">Lorem ipsum dolor sit amet, consectetur adipiscing elit, sed do eiusmod tempor incididunt ut labore et dolore mag na aliqua ipsum suspendisse ultrices gravidisus mmodo viverra maecenas accumsan lacus vel facilisis</p>
<div class="abs quote-name">MARLON REYES</div>

<!-- why choose -->
<div class="abs why-photo"></div>
<div class="abs why-inner" role="img" aria-label="Photo of dialysis equipment in soft teal tones"></div>
<h2 class="abs heading h2" style="left:596px;top:3352px"><span class="c-blue">Why Choose</span><br><span class="c-green">Torvane Health?</span></h2>
<div class="abs body-copy" style="left:629px;top:3466px;width:410px">
  <p>Lorem ipsum dolor sit amet, consectetur adipiscing elit, sed do eiusmod tempor incididunt ut laboreet dolore magna aliqua. Quis ipsum suspendisse ultrices gravida. Risus commodo viverra maece nas accumsan lacus vel facilisis.</p>
  <p style="margin-top:21px">Lorem ipsum dolor sit amet, consectetur adipiscin gelit, sed do eiusmod tempor incididunt ut laboret dolore magna aliqua. Quis ipsum suspendisse ultrices gravida. Risus commodo viverra maece nas accumsan lacus vel facilisis.</p>
</div>

<!-- footer -->
<footer class="abs footer"></footer>
<div class="abs foot-brand"><i class="mark"></i><span class="name">TORVANE<br>HEALTH</span></div>

<h4 class="abs foot-h" style="left:380px">Location 1</h4>
<div class="contact-row" style="left:383px;top:3998px">
  <span class="ico"><svg width="16" height="16" viewBox="0 0 24 24" fill="none" stroke="#fff" stroke-width="2"><path d="M12 22s7-7 7-12a7 7 0 0 0-14 0c0 5 7 12 7 12z"/><circle cx="12" cy="10" r="2.5"/></svg></span>
  <span>Location: Port Calder<br>Lorem placeholder5767</span>
</div>
<div class="contact-row" style="left:383px;top:4062px">
  <span class="ico"><svg width="16" height="16" viewBox="0 0 24 24" fill="none" stroke="#fff" stroke-width="2"><rect x="3" y="5" width="18" height="14"/><path d="M3 6l9 7 9-7"/></svg></span>
  <span>Email:<br>info@torvanehealth.com</span>
</div>
<div class="contact-row" style="left:383px;top:4126px">
  <span class="ico"><svg width="16" height="16" viewBox="0 0 24 24" fill="none" stroke="#fff" stroke-width="2"><path d="M5 3h4l2 5-3 2a12 12 0 0 0 6 6l2-3 5 2v4a2 2 0 0 1-2 2A17 17 0 0 1 3 5a2 2 0 0 1 2-2z"/></svg></span>
  <span>Phone:<br>555 019 4410</span>
</div>

<h4 class="abs foot-h" style="left:660px">Location 2</h4>
<div class="contact-row" style="left:663px;top:3998px">
  <span class="ico"><svg width="16" height="16" viewBox="0 0 24 24" fill="none" stroke="#fff" stroke-width="2"><path d="M12 22s7-7 7-12a7 7 0 0 0-14 0c0 5 7 12 7 12z"/><circle cx="12" cy="10" r="2.5"/></svg></span>
  <span>Location: Halvern Isle<br>Lorem placeholder 5767</span>
</div>
<div class="contact-row" style="left:663px;top:4062px">
  <span class="ico"><svg width="16" height="16" viewBox="0 0 24 24" fill="none" stroke="#fff" stroke-width="2"><rect x="3" y="5" width="18" height="14"/><path d="M3 6l9 7 9-7"/></svg></span>
  <span>Email:<br>info@torvanehealth.com</span>
</div>
<div class="contact-row" style="left:663px;top:4126px">
  <span class="ico"><svg width="16" height="16" viewBox="0 0 24 24" fill="none" stroke="#fff" stroke-width="2"><path d="M5 3h4l2 5-3 2a12 12 0 0 0 6 6l2-3 5 2v4a2 2 0 0 1-2 2A17 17 0 0 1 3 5a2 2 0 0 1 2-2z"/></svg></span>
  <span>Phone:<br>555 019 4410</span>
</div>

<h4 class="abs foot-h" style="left:941px">Links</h4>
<ul class="abs links">
  <li>Home</li><li>About Us</li><li>Services</li><li>Patient Information</li><li>Resources</li><li>Contact Us</li><li>Testimonials</li>
</ul>
<div class="abs foot-rule"></div>
<p class="abs copyright">Copyright© 2024 Torvane Health. All Rights Reserved.</p>

</body>
</html>
```